Www.zapdeck.com monthly sweepstakes.

Every month I am giving away 1st place $500 gift card to your local RC hobby shop of choice, 2nd place $100 gift card 3rd place ZapDeck merch. All things rc: cars, boats, quadcopters, helicopters, airplanes.

Needs to be with the color theme of the website. Check zapdeck.com for current sweepstakes banner. New banner should be half the size in height. I will post dimension later.

Target Market(s)

Rc hobbies cars airplanes helicopters boats

Industry/Entity Type

RemoteControl hobbies

Requirements
Must have
• 1440x680 size, Blend with black background, creative and in incorporate all trypes of rc craft
Should not have
• To many different colors, dosnt need logo as its already on website. This is a banner for my homepage

```html
<!DOCTYPE html>
<html lang="en">
<head>
<meta charset="utf-8">
<title>ZapDeck Monthly Sweepstakes Banner</title>
<link rel="stylesheet" href="https://fonts.googleapis.com/css2?family=Exo+2:ital,wght@0,800;0,900;1,900&family=Montserrat:wght@400;800&display=swap">
<style>
:root{
  --page:#ffffff;
  --black:#0a0a0b;
  --red:#e0141b;
  --red-deep:#7a0a0e;
  --red-glow:rgba(200,20,30,.55);
  --white:#ffffff;
  --ink:#1a1a1a;
  --silver-hi:#f2f2f2;
  --silver-lo:#9a9a9a;
  --gold-hi:#f4d46a;
  --gold-lo:#b88a1c;
}
*{margin:0;padding:0;box-sizing:border-box}
html,body{width:1200px;height:666px;overflow:hidden;background:var(--page)}
.banner{
  position:absolute;left:0;top:49px;width:1200px;height:567px;
  background:var(--black);overflow:hidden;
  font-family:"Montserrat",Arial,sans-serif;color:var(--white);
}
.banner__glow{
  position:absolute;inset:0;
  background:
    radial-gradient(ellipse 360px 120px at 600px 250px,rgba(120,10,40,.55),transparent 70%),
    linear-gradient(180deg,#0d0d0f 0%,#17090c 55%,#0b0b0c 100%);
}
.smoke{position:absolute;border-radius:50%;filter:blur(18px)}
.smoke--left{left:30px;top:40px;width:220px;height:460px;background:radial-gradient(closest-side,var(--red-glow),transparent)}
.smoke--right{right:30px;top:60px;width:200px;height:300px;background:radial-gradient(closest-side,var(--red-glow),transparent)}
.frame{position:absolute;inset:0}
.headline{
  position:absolute;left:0;right:0;text-align:center;
  font-family:"Exo 2",Impact,sans-serif;font-weight:900;font-style:italic;
  line-height:1;letter-spacing:-1px;text-transform:uppercase;
}
.headline--top{top:72px;font-size:90px;transform:translateX(-6px)}
.headline--top .plain{
  color:var(--white);
  text-shadow:2px 0 0 var(--red),-2px 0 0 var(--red),0 2px 0 var(--red),0 -2px 0 var(--red),
              2px 2px 0 var(--red),-2px -2px 0 var(--red),2px -2px 0 var(--red),-2px 2px 0 var(--red);
}
.headline--top .accent{
  color:var(--red);
  text-shadow:2px 0 0 var(--white),-2px 0 0 var(--white),0 2px 0 var(--white),0 -2px 0 var(--white),
              2px 2px 0 var(--white),-2px -2px 0 var(--white),2px -2px 0 var(--white),-2px 2px 0 var(--white);
}
.headline--bottom{top:160px;font-size:88px;color:var(--white);text-shadow:0 4px 0 #000}
.craft{position:absolute;border-radius:30px}
.craft--jet{left:16px;top:263px;width:304px;height:122px;background:linear-gradient(90deg,#bfc3c8,#b3141c 60%,#d9d9d9);border-radius:40px 60px 20px 20px}
.craft--car{left:77px;top:394px;width:228px;height:112px;background:linear-gradient(180deg,#8f0d13,#2a2a2a)}
.craft--drone{left:931px;top:226px;width:206px;height:140px;background:linear-gradient(135deg,#d2232a,#d8dde4 55%,#b81a22)}
.craft--truck{left:875px;top:366px;width:238px;height:164px;background:linear-gradient(180deg,#d9d9d9 0%,#b2121a 35%,#2a2a2a 100%)}
.prize{
  position:absolute;border:3px solid var(--red);border-radius:18px;
  background:linear-gradient(180deg,#1d1d20 0%,#050506 100%);
  box-shadow:0 0 18px rgba(224,20,27,.35);
  text-align:center;
}
.prize--second{left:282px;top:294px;width:192px;height:198px}
.prize--first{left:490px;top:268px;width:218px;height:224px}
.prize--third{left:726px;top:294px;width:187px;height:198px}
.prize__amount{font-family:"Exo 2",sans-serif;font-weight:800;line-height:1}
.prize__amount sup{font-size:.45em;vertical-align:.9em}
.prize--second .prize__amount{font-size:44px;margin-top:56px}
.prize--first .prize__amount{font-size:50px;margin-top:64px}
.prize__title{font-family:"Exo 2",sans-serif;font-weight:800;font-size:22px;line-height:1.1}
.prize--first .prize__title{font-size:24px}
.prize__note{font-size:13px;line-height:1.2;margin-top:8px;font-weight:400}
.prize--third .prize__title{font-size:26px;margin-top:70px;line-height:1.05}
.ribbon{position:absolute;overflow:visible}
.ribbon text{font-family:"Exo 2",sans-serif;font-weight:900;font-size:20px}
</style>
</head>
<body>
<main class="banner" aria-label="ZapDeck monthly sweepstakes">
  <div class="banner__glow"></div>
  <div class="smoke smoke--left" role="img" aria-label="Red smoke swirls"></div>
  <div class="smoke smoke--right" role="img" aria-label="Red smoke swirls"></div>

  <svg class="frame" width="1200" height="567" viewBox="0 0 1200 567" aria-hidden="true">
    <g fill="none" stroke="var(--red)" stroke-width="3">
      <path d="M32 150 V30 H250 l10 -8 H420 M780 22 H1135 l10 8 V150"/>
      <path d="M32 420 V540 H260 M940 540 H1145 V420" stroke-opacity=".8"/>
    </g>
    <g fill="var(--red-deep)">
      <rect x="1062" y="56" width="8" height="8"/><rect x="1076" y="56" width="8" height="8"/>
      <rect x="1090" y="56" width="8" height="8"/><rect x="1104" y="56" width="8" height="8"/>
      <rect x="1118" y="56" width="8" height="8"/>
    </g>
    <rect x="260" y="530" width="680" height="10" fill="var(--red-deep)" opacity=".6"/>
  </svg>

  <h1 class="headline headline--top"><span class="plain">WIN</span> <span class="accent">AN RC</span></h1>
  <p class="headline headline--bottom">SHOPPING SPREE!</p>

  <div class="craft craft--jet" role="img" aria-label="Red and white RC jet"></div>
  <div class="craft craft--car" role="img" aria-label="Red RC formula car"></div>
  <div class="craft craft--drone" role="img" aria-label="Red racing quadcopter"></div>
  <div class="craft craft--truck" role="img" aria-label="Red RC buggy"></div>

  <section class="prize prize--second">
    <p class="prize__amount"><sup>$</sup>100</p>
    <p class="prize__title">GIFT CARD</p>
    <p class="prize__note">TO YOUR LOCAL<br>HOBBY SHOP.</p>
  </section>
  <section class="prize prize--first">
    <p class="prize__amount"><sup>$</sup>500</p>
    <p class="prize__title">GIFT CARD</p>
    <p class="prize__note">TO YOUR LOCAL<br>HOBBY SHOP.</p>
  </section>
  <section class="prize prize--third">
    <p class="prize__title">ZAPDECK<br>MERCH</p>
  </section>

  <svg class="ribbon" style="left:262px;top:266px" width="232" height="84" viewBox="0 0 232 84">
    <defs><linearGradient id="silver" x1="0" y1="0" x2="0" y2="1"><stop offset="0" stop-color="var(--silver-hi)"/><stop offset="1" stop-color="var(--silver-lo)"/></linearGradient>
    <path id="arcSilver" d="M30 62 Q116 26 202 62"/></defs>
    <path d="M4 68 L30 50 L24 76 Z M228 68 L202 50 L208 76 Z" fill="var(--silver-lo)"/>
    <path d="M22 44 Q116 8 210 44 L206 70 Q116 36 26 70 Z" fill="url(#silver)"/>
    <text fill="var(--ink)"><textPath href="#arcSilver" startOffset="50%" text-anchor="middle">2ND PLACE</textPath></text>
  </svg>
  <svg class="ribbon" style="left:470px;top:234px" width="258" height="84" viewBox="0 0 258 84">
    <defs><linearGradient id="crimson" x1="0" y1="0" x2="0" y2="1"><stop offset="0" stop-color="#ff2a30"/><stop offset="1" stop-color="#9c0c12"/></linearGradient>
    <path id="arcRed" d="M32 62 Q129 24 226 62"/></defs>
    <path d="M4 68 L32 50 L26 78 Z M254 68 L226 50 L232 78 Z" fill="var(--red-deep)"/>
    <path d="M24 44 Q129 6 234 44 L230 70 Q129 34 28 70 Z" fill="url(#crimson)"/>
    <text fill="var(--white)"><textPath href="#arcRed" startOffset="50%" text-anchor="middle">1ST PLACE</textPath></text>
  </svg>
  <svg class="ribbon" style="left:704px;top:266px" width="232" height="84" viewBox="0 0 232 84">
    <defs><linearGradient id="gold" x1="0" y1="0" x2="0" y2="1"><stop offset="0" stop-color="var(--gold-hi)"/><stop offset="1" stop-color="var(--gold-lo)"/></linearGradient>
    <path id="arcGold" d="M30 62 Q116 26 202 62"/></defs>
    <path d="M4 68 L30 50 L24 76 Z M228 68 L202 50 L208 76 Z" fill="var(--gold-lo)"/>
    <path d="M22 44 Q116 8 210 44 L206 70 Q116 36 26 70 Z" fill="url(#gold)"/>
    <text fill="var(--white)"><textPath href="#arcGold" startOffset="50%" text-anchor="middle">3RD PLACE</textPath></text>
  </svg>
</main>
</body>
</html>
```